Gift Card Design - Suds Harbor Co

I am needing a design for a standard plastic gift card, (ever so slightly large then a standard rounded edge business card). Name of the business is Suds Harbor Co. Attached is a file with a poor example, done by an equipment manufacturing firm, that I feel could be much better. Simple, clean and classy with what it is and does along with our name is what I am looking for. Attached also is out logo and source of logo, they don't have to be on the card.

Target Market(s)

Car wash customers in an upscale market.

Industry/Entity Type

Business

Font styles to use
Serif
Other font styles liked:
• whatever you feel, but I do like the font on a Brevanto golf ball

Requirements
Must have
• Words anywhere on the card -
• Reloadable Card
• Self Serve Bays & Vacuums.
• Also need name of the business, Suds Harbor Co.
Nice to have
• Work in Pantone #7483 as there is existing signage with that as a primary color, just trying to tie things together. Attached is my business logo and a picture of the source of the logo, you do not have to use those if you don't want to. I do like clean and classy but am open to creativity, that's why I am submitting this project.
Should not have
• Naked lady pictures

```html
<!DOCTYPE html>
<html lang="en">
<head>
<meta charset="utf-8">
<title>Suds Harbor Co — Reloadable Card</title>
<link rel="stylesheet" href="https://fonts.googleapis.com/css2?family=Tinos:wght@400;700&display=swap">
<style>
  :root {
    --stage: #e4e4e4;
    --card-green: #2e4d3b;
    --card-green-deep: #264532;
    --card-green-light: #3f6450;
    --band-green: #1f4c31;
    --title-band: rgba(140, 180, 155, 0.28);
    --tan: #b1845a;
    --soft-text: #93b09f;
  }
  html, body {
    margin: 0;
    padding: 0;
    width: 1200px;
    height: 1200px;
    overflow: hidden;
    background: var(--stage);
  }
  .gift-card {
    position: absolute;
    left: 40px;
    top: 253px;
    width: 1120px;
    height: 694px;
    display: block;
  }
  .card-title {
    font-family: "Tinos", "Times New Roman", serif;
    font-weight: 700;
    font-size: 70px;
    fill: var(--tan);
    letter-spacing: 1px;
  }
  .card-subtitle,
  .card-services {
    font-family: "Tinos", "Times New Roman", serif;
    font-weight: 400;
    font-size: 48px;
    fill: var(--soft-text);
    letter-spacing: 1px;
  }
  .brand-mark-name {
    font-family: "Tinos", "Times New Roman", serif;
    font-weight: 700;
    font-size: 34px;
    fill: var(--tan);
  }
</style>
</head>
<body>
<svg class="gift-card" viewBox="0 0 1060 657" xmlns="http://www.w3.org/2000/svg">
  <defs>
    <clipPath id="card-shape">
      <rect x="0" y="0" width="1060" height="657" rx="32" ry="32"/>
    </clipPath>
    <linearGradient id="facet-tone" x1="0" y1="0" x2="1" y2="1">
      <stop offset="0" stop-color="var(--card-green-deep)"/>
      <stop offset="0.45" stop-color="var(--card-green-light)"/>
      <stop offset="1" stop-color="var(--card-green-deep)"/>
    </linearGradient>
  </defs>

  <g clip-path="url(#card-shape)">
    <rect class="card-base" x="0" y="0" width="1060" height="657" fill="var(--card-green)"/>
    <rect class="card-texture" x="0" y="0" width="1060" height="570" fill="url(#facet-tone)" opacity="0.7"
          role="img" aria-label="Soft faceted green geometric background texture"/>

    <rect class="title-band" x="0" y="70" width="755" height="107" fill="var(--title-band)"/>
    <rect class="services-band" x="0" y="570" width="1060" height="87" fill="var(--band-green)"/>

    <path class="ribbon-top" d="M755 0 H967 V255 L862 207 L755 255 Z" fill="var(--tan)"/>
    <rect class="ribbon-bottom" x="755" y="570" width="212" height="87" fill="var(--tan)"/>
  </g>

  <text class="card-title" x="370" y="144" text-anchor="middle">Suds Harbor Co</text>
  <text class="card-subtitle" x="370" y="225" text-anchor="middle">Reloadable Card</text>
  <text class="card-services" x="370" y="624" text-anchor="middle">Self Serve &amp; Vacuums</text>

  <g class="brand-mark">
    <circle cx="862" cy="360" r="46" fill="none" stroke="var(--tan)" stroke-width="4"/>
    <text class="brand-mark-name" x="862" y="452" text-anchor="middle">Suds Harbor Co</text>
  </g>
</svg>
</body>
</html>
```